flat health bread wrap

PREFERENCE WILL BE GIVEN TO DESIGNERS WHO CAN SUBMIT THEIR INITIAL IDEAS PRIOR TO 9.00AM FRIDAY 12TH AUGUST 2010 MELBOURNE AUSTRALIA TIME!

additonal packaging information

target market:

mothers who make their childrens lunch, people looking for a healthy alternative and a change to normal bread,

pack size

34cm length X 28.5cm width
crystal-clear, see through plastic re-sealable zip lock pack.

brand name: tidy fold
product explanation: mediterranean flat bread
product features: see below
raw product size: 22cm X 22cm SQUARE
most US products of this style are round or oval! ours will be new to the US market.
colour: pale pita bread colour
markings on bread: pale fried hotplate markings
number of pieces per pack: 8
gross weight of product 250 grams
product manufactured in melbourne australia
accreditations: kosher and halal

front of pack: good design and accreditations (KOSHER AND HALAL)

back of pack: barcode, how to wrap instructions,
US nutritional panel, ingredient list (flour, water, salt and vitamins. gluten allegen warning. oxygen absorbing sachet warning (do not eat)
company address and contact details,

3 flavours: Rye, White, wholmeal and Corn.

marketing
new product designed specificaly for the US market,
distribution: supermarkets, health food stores
retail price: USD $2.99

# New Middle Eastern style Healthy Valley Loaf Wraps. (Tortillas)
# Square flat bread sheets
# For distribution across USA
# Targetting
* Health food enthusiats
* New Age consumers
* Mothers looking for lunchbox options
* Those seeking a substitute for the traditional lunch sandwich
* These square flat bread sheets replace the traditional bread made sandwich

These products are:
# Shelf stable (minimum 6 months) without refrigeration
# Completely free of:
- preservatives
- colours
- yeast
- cholesterol
- trans fats
- hydrogenated oils
# soft and pliable, and extremely thin
# made from wheat/rye/corn flour, water and salt AND NOTHING ELSE
# organic and other options available
# manufactured in Melbourne Australia
# Kosher and Halal certified

Our proposed brand name is TIDY FOLD
# we prefer to dwell on the humourous perspectives of the name
# our product will look something like these - http://www.valleyloaf.com.au/cgi-bin/index.pl?menu_id=3
and these http://www.sunpathovens.com.au/sorj.html

# This range is unique
in that it is without additives preservatives etc
is NOT round but square in shape
^ we wouold like to emphasise this
^ packaged in transparent zip-lock bags

Reason: we would like to have a better idea of our package design for our meeting 9.00am friday 12th august. MELBOURNE AUSTRALIA TIME!

dear wanda,

we have already guaranteed $260.00. 

we expect to spend about $1,000-1,500 for this design project by the time we have accepted someone from the contest.

things that still need to be completed in 4 flavours...... and we will pay for! 
1. barcode
2. text
3. US nutritional panel
4. how to wrap instructions
5. ingredient lists
6. etc.
It's not about the money, money, money,
We don't need your money, money, money.
We just wanna make the world dance,
Forget about the price tag.
Ain't about the (ha!) cha-ching cha-ching.
Ain't about the (yeah!) ba-bling ba-bling,
Wanna make the world dance,

Read more: http://artists.hummalong.com/rosa-q-lyrics-paper-kite-feat-dv-k-qj87npv#ixzz1V4GpF9lq 
HumAlong - Your favorite Music Community 

tobias

Reason: only 5 designers (16 designs) have submitted work for assessment out of 37,000! I will award contest at the end of the extended 7 days tobias

Reason: because I can and the entries received to date are un satisfactory! tobias

our competitors in australia. see there packs in the links below

http://www.valleyloaf.com.au
http://www.balitro.com.au/wv_softwraps.aspx
http://www.qrnfoods.com.au/bravolis2/index.php?option=com_zoo&view=item&Itemid=204

• i FORGOT, THE PRODUCT IS DISPLAYED IN 2 WAYS

1. ABOVE THE ZIP LOCK CLOSE TO THE TOP 2 CORNERS ARE HANGING HOLES. THE PRODUCT SWINGS FROM 2 HOOKS IN A SUPER MARKET

2. THE PRODUCT IS STACKED. ONE ON TOP OF THE OTHER.

IN A SHELF
• HEALTHY, GREEN COLOURS, BROWNS, CREAMS, SOFT FONTS, LOGO OR SYMBOL? i DO NOT REALLY KNOW!
• BRIGHT COLOURS! SCREAMING HEADLINES!

KEEP IN MIND THE SQUARE SHAPE PRODUCT AND THE PRODUCT COLOUR WILL BE SEEN THROUGH THE CLEAR PACK

```html
<!DOCTYPE html>
<html lang="en">
<head>
<meta charset="utf-8">
<title>tidy fold – mediterranean flat bread packaging</title>
<link href="https://fonts.googleapis.com/css2?family=Open+Sans:ital,wght@0,300;0,400;0,600;0,700;1,400&family=Roboto+Condensed:wght@400;700&family=Lora:ital@1&family=Arimo:wght@400;700;800&display=swap" rel="stylesheet">
<style>
  :root {
    --stage: #e6e7e8;
    --glow: #ffffff;
    --kraft-dark: #a4744c;
    --kraft-light: #c6ad8e;
    --kraft-mid: #b38a63;
    --edge-dark: #4e3019;
    --brand-brown: #4a2c17;
    --ink: #2a1a0e;
    --paper: #ffffff;
    --recycle: #3f8f3a;
  }
  * { box-sizing: border-box; margin: 0; padding: 0; }
  html, body { width: 1200px; height: 848px; overflow: hidden; }
  body {
    position: relative;
    background:
      radial-gradient(ellipse 420px 380px at 430px 420px, var(--glow) 55%, transparent 100%),
      radial-gradient(ellipse 330px 380px at 950px 420px, var(--glow) 55%, transparent 100%),
      var(--stage);
    font-family: "Open Sans", sans-serif;
  }

  .panel {
    position: absolute;
    top: 94px;
    height: 624px;
    background: linear-gradient(118deg, var(--kraft-dark) 0%, var(--kraft-mid) 30%, var(--kraft-light) 52%, var(--kraft-mid) 75%, var(--kraft-dark) 100%);
  }
  .panel--front { left: 252px; width: 368px; }
  .panel--back { left: 768px; width: 356px; }

  .front-edge {
    position: absolute; left: 0; top: 0; width: 9px; height: 100%;
    background: linear-gradient(180deg, #7a5233, var(--edge-dark));
  }
  .swoosh { position: absolute; }

  .accreditation {
    position: absolute; left: 33px; top: 22px;
    color: var(--paper); font-size: 10px;
  }
  .flavour {
    position: absolute; left: 288px; top: 6px;
    font-family: "Lora", serif; font-style: italic;
    font-size: 36px; color: var(--brand-brown);
  }
  .brand-name {
    position: absolute; left: 152px; top: 214px;
    font-family: "Open Sans", sans-serif; font-weight: 300;
    color: var(--brand-brown); line-height: 1;
  }
  .brand-name__first { display: block; font-size: 140px; letter-spacing: -2px; }
  .brand-name__second { position: absolute; left: 230px; top: 150px; font-size: 64px; white-space: nowrap; }
  .product-line {
    position: absolute; left: 84px; bottom: 14px;
    font-size: 19px; color: var(--brand-brown);
  }

  .price {
    position: absolute; left: 21px; top: 22px;
    color: var(--paper); font-size: 22px;
  }
  .features {
    position: absolute; left: 20px; top: 118px; width: 190px;
    font-family: "Roboto Condensed", sans-serif; font-size: 8.6px;
    line-height: 10.6px; color: var(--ink); list-style: none;
  }
  .fold-steps {
    position: absolute; left: 20px; top: 278px; width: 190px;
    font-family: "Roboto Condensed", sans-serif; font-size: 8.6px;
    line-height: 11.5px; color: var(--ink);
  }
  .origin {
    position: absolute; left: 24px; top: 410px;
    font-family: "Arimo", sans-serif; font-weight: 700;
    font-size: 14.5px; line-height: 19px; color: #000;
  }
  .code-area {
    position: absolute; left: 20px; top: 543px; width: 188px; height: 63px;
    background: var(--paper);
  }
  .weight {
    position: absolute; left: 275px; top: 587px;
    font-size: 13px; color: var(--ink);
  }
  .recycle-mark {
    position: absolute; left: 323px; top: 582px; width: 16px; height: 16px;
    border-radius: 50%; background: var(--recycle);
  }

  .nutrition {
    position: absolute; left: 205px; top: 110px; width: 120px; height: 281px;
    background: var(--paper); border: 1px solid #000; padding: 3px 4px;
    font-family: "Arimo", sans-serif; color: #000;
    font-size: 5.6px; line-height: 8.2px;
  }
  .nutrition__title { font-weight: 800; font-size: 13px; line-height: 14px; letter-spacing: -0.2px; }
  .nutrition__row { display: flex; justify-content: space-between; border-top: 0.6px solid #000; }
  .nutrition__row--indent { padding-left: 6px; }
  .nutrition__bar { height: 5px; background: #000; margin: 1px 0; }
  .nutrition__bar--mid { height: 2.5px; }
  .nutrition strong { font-weight: 700; }
  .nutrition__right { text-align: right; }
  .nutrition__note { font-size: 4.6px; line-height: 6px; border-top: 0.6px solid #000; padding-top: 1px; }
  .nutrition__mini { display: grid; grid-template-columns: 1.5fr 1fr 0.6fr 0.6fr; font-size: 4.6px; line-height: 6px; border-top: 0.6px solid #000; }
  .nutrition__foot { font-size: 4.6px; line-height: 6px; text-align: center; border-top: 0.6px solid #000; }
</style>
</head>
<body>

<section class="panel panel--front" aria-label="Front of pack">
  <div class="front-edge"></div>
  <p class="accreditation">Kosher and Halal</p>
  <p class="flavour">rye</p>
  <svg class="swoosh" style="left:197px;top:38px" width="171" height="56" viewBox="0 0 171 56">
    <path d="M0 52 C50 28 110 10 171 14 L171 20 C115 20 60 34 0 54 Z" fill="#ffffff"/>
  </svg>
  <p class="product-line">mediterranean flat bread</p>
</section>

<h1 class="brand-name">
  <span class="brand-name__first">Tidy</span>
  <span class="brand-name__second">fold</span>
</h1>

<section class="panel panel--back" aria-label="Back of pack">
  <p class="price">$ 2.99</p>
  <svg class="swoosh" style="left:28px;top:40px" width="110" height="54" viewBox="0 0 110 54">
    <path d="M0 14 C40 10 80 26 110 50 L110 54 C78 34 40 20 0 18 Z" fill="#ffffff"/>
  </svg>

  <ul class="features">
    <li>Shelf stable (minimum 6 months) without refrigeration</li>
    <li>Completely free of:</li>
    <li>- preservatives</li>
    <li>- colours</li>
    <li>- yeast</li>
    <li>- cholesterol</li>
    <li>- trans fats</li>
    <li>- hydrogenated oils</li>
    <li>Soft and pliable, and extremely thin</li>
    <li>Made from wheat/rye/corn flour, water and salt</li>
    <li>AND NOTHING ELSE</li>
  </ul>

  <div class="fold-steps">
    <p>How to fold instructions:</p>
    <p>Add ingredients on to the bread.</p>
    <p>Fold flat bread and tightly roll up.</p>
  </div>

  <div class="nutrition" aria-label="Nutrition Facts">
    <p class="nutrition__title">Nutrition Facts</p>
    <p>Serving Size 1/2 cup (about 82g)</p>
    <p>Servings Per Container 8</p>
    <div class="nutrition__bar"></div>
    <p>Amount Per Serving</p>
    <div class="nutrition__row"><span><strong>Calories</strong> 200</span><span>Calories from Fat 130</span></div>
    <div class="nutrition__bar nutrition__bar--mid"></div>
    <p class="nutrition__right">% Daily Value*</p>
    <div class="nutrition__row"><span><strong>Total Fat</strong> 14g</span><strong>22%</strong></div>
    <div class="nutrition__row nutrition__row--indent"><span>Saturated Fat 9g</span><strong>45%</strong></div>
    <div class="nutrition__row nutrition__row--indent"><span>Trans Fat 0g</span><span></span></div>
    <div class="nutrition__row"><span><strong>Cholesterol</strong> 55mg</span><strong>18%</strong></div>
    <div class="nutrition__row"><span><strong>Sodium</strong> 40mg</span><strong>2%</strong></div>
    <div class="nutrition__row"><span><strong>Total Carbohydrate</strong> 17g</span><strong>6%</strong></div>
    <div class="nutrition__row nutrition__row--indent"><span>Dietary Fiber 1g</span><strong>4%</strong></div>
    <div class="nutrition__row nutrition__row--indent"><span>Sugars 14g</span><span></span></div>
    <div class="nutrition__row"><span><strong>Protein</strong> 3g</span><span></span></div>
    <div class="nutrition__bar"></div>
    <div class="nutrition__row"><span>Vitamin A 10%</span><span>• Vitamin C 0%</span></div>
    <div class="nutrition__row"><span>Calcium 10%</span><span>• Iron 6%</span></div>
    <p class="nutrition__note">*Percent Daily Values are based on a 2,000 calorie diet. Your daily values may be higher or lower depending on your calorie needs.</p>
    <div class="nutrition__mini">
      <span></span><span>Calories</span><span>2,000</span><span>2,500</span>
      <span>Total Fat</span><span>Less than</span><span>65g</span><span>80g</span>
      <span>Sat Fat</span><span>Less than</span><span>20g</span><span>25g</span>
      <span>Cholesterol</span><span>Less than</span><span>300mg</span><span>300mg</span>
      <span>Sodium</span><span>Less than</span><span>2,400mg</span><span>2,400mg</span>
      <span>Total Carb</span><span></span><span>300g</span><span>375g</span>
      <span>Fiber</span><span></span><span>25g</span><span>30g</span>
    </div>
    <p class="nutrition__foot">Calories per gram: Fat 9 • Carbohydrate 4 • Protein 4</p>
  </div>

  <p class="origin">Product manufactured:<br>Melbourne Australia</p>
  <div class="code-area"></div>
  <p class="weight">250 gr</p>
  <div class="recycle-mark" aria-label="Recycling mark"></div>
</section>

</body>
</html>
```